Need Letterhead and Business Card

I have a logo but i need new letterhead and biz cards. We are a real estate investment firm so we need very professional but also do not want to be old fashioned. We have 3 locations; Singapore, New York and Ponte Vedra Florida. I can provide full addresses if needed. If you have adjustments to our logo you would recommend we are open to them.
I will be putting in a separate project but we also need a template for our own powerpoint slide presentations and website.

Industry/Entity Type

Real Estate

```html
<!DOCTYPE html>
<html lang="en">
<head>
<meta charset="utf-8">
<title>Halden Business Cards</title>
<link rel="stylesheet" href="https://fonts.googleapis.com/css2?family=Marcellus&display=swap">
<style>
  :root {
    --navy: #0f4483;
    --navy-deep: #0b3770;
    --gold: #d3a417;
    --white: #ffffff;
    --paper: #f4f4f2;
    --ground: #2a2a2a;
    --text-light: #e9eef6;
  }
  * { margin: 0; padding: 0; box-sizing: border-box; }
  html, body { width: 1200px; height: 900px; overflow: hidden; background: var(--ground); }
  body { position: relative; font-family: "Marcellus", "Optima", sans-serif; }

  .card {
    position: absolute;
    width: 660px; height: 380px;
    left: 270px;
    overflow: hidden;
    box-shadow: 0 10px 30px rgba(0,0,0,.5);
  }
  .card--back { top: 45px; }
  .card--front { top: 475px; }
  .card svg.card__art { position: absolute; inset: 0; width: 100%; height: 100%; }

  .brand { position: absolute; text-align: left; }
  .brand__name {
    display: block;
    color: var(--navy);
    font-size: 74px;
    letter-spacing: 2px;
    line-height: 1;
  }
  .brand__rule { display: block; height: 2px; background: var(--navy); margin: 6px 0 4px; }
  .brand__tagline {
    display: block;
    color: var(--gold);
    font-size: 13.5px;
    letter-spacing: .5px;
    white-space: nowrap;
  }
  .card--back .brand { left: 345px; top: 120px; }
  .card--front .brand { left: 200px; top: 55px; }

  .offices { position: absolute; left: 34px; top: 100px; color: var(--text-light); font-size: 15px; line-height: 1.15; }
  .offices li { list-style: none; margin-bottom: 10px; white-space: nowrap; }

  .person { position: absolute; left: 40px; top: 275px; color: var(--white); }
  .person__name { font-size: 24px; font-weight: 400; }
  .person__title { font-size: 16px; color: var(--text-light); }
  .person__email { position: absolute; left: 40px; top: 345px; color: var(--text-light); font-size: 16px; display: flex; align-items: center; gap: 8px; }

  .contact { position: absolute; left: 420px; top: 225px; color: var(--text-light); font-size: 15px; }
  .contact li { list-style: none; display: flex; align-items: center; gap: 10px; height: 22px; }
  .contact__office { font-size: 15px; letter-spacing: .5px; color: var(--white); }
  .icon { width: 14px; height: 14px; flex: none; fill: var(--gold); }
</style>
</head>
<body>

<section class="card card--back">
  <svg class="card__art" viewBox="0 0 660 380" aria-hidden="true">
    <rect width="660" height="380" fill="var(--navy)"/>
    <path d="M410 0 Q215 150 160 380 L660 380 L660 0 Z" fill="var(--gold)"/>
    <path d="M450 0 Q255 165 200 380 L660 380 L660 0 Z" fill="var(--paper)"/>
  </svg>
  <ul class="offices">
    <li>123 Fake Street<br>Anytown, Singapore</li>
    <li>123 Fake Street<br>Anytown, New York</li>
    <li>123 Fake Street<br>Anytown, Ponte Vedra</li>
  </ul>
  <div class="brand">
    <span class="brand__name">HALDEN</span>
    <span class="brand__rule"></span>
    <span class="brand__tagline">REAL ESTATE INVESTMENT &amp; MANAGEMENT</span>
  </div>
</section>

<section class="card card--front">
  <svg class="card__art" viewBox="0 0 660 380" aria-hidden="true">
    <rect width="660" height="380" fill="var(--paper)"/>
    <path d="M0 255 Q340 245 660 125 L660 380 L0 380 Z" fill="var(--navy)"/>
    <path d="M250 238 Q480 205 660 105 L660 122 Q480 220 250 238 Z" fill="var(--gold)"/>
  </svg>
  <div class="brand">
    <span class="brand__name">HALDEN</span>
    <span class="brand__rule"></span>
    <span class="brand__tagline">REAL ESTATE INVESTMENT &amp; MANAGEMENT</span>
  </div>

  <div class="person">
    <h1 class="person__name">Daniel Marlowe</h1>
    <p class="person__title">managing director</p>
  </div>
  <p class="person__email">
    <svg class="icon" viewBox="0 0 14 14"><path d="M1 3h12v8H1z M1 3l6 5 6-5" fill="var(--gold)" stroke="var(--navy)" stroke-width="1"/></svg>
    dmarlowe@haldenrealestate.com
  </p>

  <ul class="contact">
    <li class="contact__office">
      <svg class="icon" viewBox="0 0 14 14"><path d="M7 0a5 5 0 0 0-5 5c0 4 5 9 5 9s5-5 5-9a5 5 0 0 0-5-5zm0 7a2 2 0 1 1 0-4 2 2 0 0 1 0 4z"/></svg>
      NEW YORK OFFICE
    </li>
    <li>
      <svg class="icon" viewBox="0 0 14 14"><path d="M4 0h6a1 1 0 0 1 1 1v12a1 1 0 0 1-1 1H4a1 1 0 0 1-1-1V1a1 1 0 0 1 1-1zm0 2v9h6V2z"/></svg>
      888 888 88 88
    </li>
    <li>
      <svg class="icon" viewBox="0 0 14 14"><path d="M3 0h8v4H3z M0 5h14v6h-3v3H3v-3H0z M4 9v4h6V9z"/></svg>
      555 555 55 55
    </li>
    <li>
      <svg class="icon" viewBox="0 0 14 14"><circle cx="7" cy="7" r="6.5"/><path d="M0.5 7h13 M7 .5v13 M7 .5c-3 3-3 10 0 13 M7 .5c3 3 3 10 0 13" stroke="var(--navy)" stroke-width="1" fill="none"/></svg>
      www.haldenrealestate.com
    </li>
  </ul>
</section>

</body>
</html>
```